Vantor Ridge needs a Business Card Design

We need a business card design for an Information Technology company based in Fairfax Virginia called Vantor Ridge. We want the business card to use our logo colors. We need it to be double-sided. The business card needs to look professional but we would like it to be unique. You can get company information from our web site (http://www.vantorridgellc.example).

Target Market(s)

Target market is Government Agencies and Business Professionals.

Industry/Entity Type

Business

Requirements
Must have
• Must have section for company name, company address, company URL, employee name, title, phone and email. Also must have company logo and space for entering logos.

```html
<!DOCTYPE html>
<html lang="en">
<head>
<meta charset="utf-8">
<title>Vantor Ridge – Business Card</title>
<link rel="stylesheet" href="https://fonts.googleapis.com/css2?family=Didact+Gothic&display=swap">
<style>
  :root {
    --stage: #dfe3e3;
    --card-white: #ffffff;
    --brand-blue: #2b2fe0;
    --brand-deep: #1e34c8;
    --ink: #3a3a3a;
  }
  * { box-sizing: border-box; margin: 0; padding: 0; }
  html, body { width: 1200px; height: 617px; overflow: hidden; }
  body {
    background: var(--stage);
    font-family: "Didact Gothic", sans-serif;
    display: flex;
    align-items: center;
    justify-content: center;
    gap: 60px;
  }
  .card {
    width: 500px;
    height: 290px;
    box-shadow: 2px 3px 8px rgba(0,0,0,0.22);
    position: relative;
    overflow: hidden;
  }
  .card-front {
    background: var(--card-white);
    display: flex;
    flex-direction: column;
    align-items: center;
    padding-top: 66px;
    color: var(--ink);
  }
  .brand { display: flex; align-items: center; gap: 12px; }
  .brand-mark { width: 34px; height: 34px; background: var(--brand-deep); }
  .brand-name { font-size: 30px; color: var(--brand-deep); letter-spacing: 0.5px; white-space: nowrap; }
  .tagline {
    font-size: 8.5px;
    letter-spacing: 0.6px;
    text-transform: uppercase;
    color: var(--brand-deep);
    margin-top: 4px;
    margin-left: 46px;
    white-space: nowrap;
  }
  .person, .company { text-align: center; font-size: 12.5px; line-height: 1.45; white-space: nowrap; }
  .person { margin-top: 36px; }
  .company { margin-top: 16px; }
  .sep { margin: 0 6px; }
  .card-back { background: var(--brand-blue); }
  .back-field {
    position: absolute; inset: 0;
    background: linear-gradient(135deg, #2f33e6 0%, #2629d4 100%);
  }
  .url-band {
    position: absolute;
    left: 70px; right: 70px; top: 131px;
    height: 38px;
    background: var(--card-white);
    display: flex; align-items: center; justify-content: center;
    font-size: 18px;
    color: var(--ink);
    white-space: nowrap;
  }
  .url-band strong { font-weight: 400; color: var(--brand-blue); }
</style>
</head>
<body>
  <section class="card card-front" aria-label="Card front">
    <div class="brand">
      <span class="brand-mark"></span>
      <span class="brand-name">Vantor Ridge</span>
    </div>
    <p class="tagline">Building clear paths to reliable systems</p>
    <div class="person">
      <p>Employee name - Company role</p>
      <p>0400 555 218<span class="sep">|</span>dana@vantorridge.example</p>
    </div>
    <div class="company">
      <p>Main Number: 555.010.2244<span class="sep">|</span>Fax: 555.010.2245</p>
      <p>4820 Meridian Way, Suite 300<span class="sep">|</span>Linden Falls, ST 00000</p>
    </div>
  </section>

  <section class="card card-back" aria-label="Card back">
    <div class="back-field" role="img" aria-label="Blue background with a tonal repeating brand pattern"></div>
    <div class="url-band">www.<strong>vantorridgellc</strong>.example</div>
  </section>
</body>
</html>
```